Storm Restoration Contractor needs a professional business card design

Looking for a professional business card design. Not looking for your cheapo MS Word standard ones that are readily available. Dont want it to be cookie cutter look like ones readily available online. We just recently changed our logo and want to freshen up all our documents. Our company handles restoring a property back to a pre-loss condition after a storm damages it. For example, wind, hail, flood, fire losses.

Target Market(s)

Property Owners, Homeowners, Property Owners, Commercial Property Owners, Property Management Companies, Hail and Wind Damaged Properties

Industry/Entity Type

Construction Company

Contact Information for Business Card

Brightline Facades
847-555-0193
847-555-0147 fax
www.brightlinefacades.example
info@brightlinefacades.example

Requirements
Must have
• Clean, Professional, fresh look
• Storm Restoration, Roofing, Siding, Windows
Nice to have
• If there is a way to incorporate storms that may be cool.

```html
<!DOCTYPE html>
<html lang="en">
<head>
<meta charset="utf-8">
<title>Brightline Facades – Business Card</title>
<link rel="stylesheet" href="https://fonts.googleapis.com/css2?family=Open+Sans:wght@400;700&display=swap">
<style>
  :root {
    --backdrop: #e9e9e7;
    --card: #ffffff;
    --brand-blue: #1572bd;
    --brand-gray: #58595b;
    --text: #3c3c3c;
    --storm-dark: #3f4650;
    --storm-mid: #7a838e;
    --storm-light: #b9bec4;
    --white: #ffffff;
  }
  * { margin: 0; padding: 0; box-sizing: border-box; }
  html, body { width: 1200px; height: 1000px; overflow: hidden; }
  body {
    background: var(--backdrop);
    font-family: "Open Sans", Arial, sans-serif;
    position: relative;
  }
  .card {
    position: absolute;
    left: 266px;
    width: 666px;
    height: 397px;
    border-radius: 22px;
    overflow: hidden;
    box-shadow: 0 4px 14px rgba(0,0,0,0.25);
  }
  .card--front { top: 74px; background: var(--card); }
  .card--back { top: 533px; }

  .accent-tab {
    position: absolute; left: 0; top: 82px;
    width: 10px; height: 39px; background: var(--brand-blue);
  }
  .holder { position: absolute; left: 32px; top: 80px; }
  .holder__name {
    color: var(--brand-blue); font-weight: 700; font-size: 21px; line-height: 28px;
  }
  .holder__role { color: var(--text); font-size: 16px; line-height: 20px; }

  .address {
    position: absolute; left: 32px; top: 146px;
    color: var(--text); font-size: 16px; line-height: 23px; font-style: normal;
  }
  .contacts {
    position: absolute; left: 32px; top: 211px; list-style: none;
    color: var(--text); font-size: 16px; line-height: 23.5px;
  }
  .contacts li { display: flex; align-items: center; gap: 5px; }
  .contacts svg { width: 16px; height: 16px; fill: var(--brand-blue); flex: none; }

  .brand {
    position: absolute; left: 326px; top: 150px;
    display: flex; align-items: center; gap: 14px;
  }
  .brand__dot {
    width: 74px; height: 74px; border-radius: 50%;
    border: 7px solid var(--brand-blue);
  }
  .brand__name {
    color: var(--brand-blue); font-weight: 700; font-size: 33px;
    line-height: 34px; text-transform: uppercase; letter-spacing: 0.5px;
  }
  .footer-band { position: absolute; left: 0; bottom: 0; width: 666px; height: 32px; }

  .storm-scene {
    position: absolute; inset: 0;
    background: linear-gradient(180deg, var(--storm-dark) 0%, var(--storm-mid) 45%, var(--storm-light) 75%, #d6d9dc 100%);
  }
  .banner {
    position: absolute; left: 0; top: 137px; width: 100%; height: 123px;
    background: rgba(40,40,40,0.55);
  }
  .brand--reversed { left: 182px; top: 146px; }
  .brand--reversed .brand__dot { border-color: var(--white); width: 66px; height: 66px; border-width: 6px; }
  .brand--reversed .brand__name { color: var(--white); font-size: 30px; line-height: 31px; }
  .services {
    position: absolute; left: 0; width: 100%; top: 233px; text-align: center;
    color: var(--white); font-size: 15px; padding-right: 70px;
  }
</style>
</head>
<body>
  <section class="card card--front">
    <div class="accent-tab"></div>
    <div class="holder">
      <div class="holder__name">ANDERS HOLMQVIST</div>
      <div class="holder__role">Founder</div>
    </div>
    <address class="address">4120 Lantern Ridge Ave 8,<br>Millbrook, MD 21000</address>
    <ul class="contacts">
      <li><svg viewBox="0 0 16 16"><path d="M2 5c0-2 3-3 6-3s6 1 6 3l-1 2-3-1V5H6v1L3 7zM4 8h8l2 6H2z"/></svg>847-555-0193</li>
      <li><svg viewBox="0 0 16 16"><path d="M4 1h8v4H4zM1 6h14v6h-3v3H4v-3H1zm4 4v4h6v-4z"/></svg>847-555-0147</li>
      <li><svg viewBox="0 0 16 16"><path d="M1 4h14v9H1zm1 1v.5l6 4 6-4V5z"/></svg>info@brightlinefacades.example</li>
      <li><svg viewBox="0 0 16 16"><circle cx="8" cy="8" r="6.5" fill="none" stroke="#1572bd" stroke-width="1.6"/><path d="M1.5 8h13M8 1.5c-3 3-3 10 0 13M8 1.5c3 3 3 10 0 13" fill="none" stroke="#1572bd" stroke-width="1.2"/></svg>www.brightlinefacades.example</li>
    </ul>
    <div class="brand">
      <div class="brand__dot"></div>
      <div class="brand__name">Brightline<br>Facades</div>
    </div>
    <svg class="footer-band" viewBox="0 0 666 32" preserveAspectRatio="none">
      <polygon points="0,0 364,0 332,32 0,32" fill="var(--brand-blue)"/>
      <polygon points="372,0 666,0 666,32 340,32" fill="var(--brand-gray)"/>
    </svg>
  </section>

  <section class="card card--back">
    <div class="storm-scene" role="img" aria-label="Photograph of a storm-damaged beach house under a grey sky, a person standing on the sand"></div>
    <div class="banner"></div>
    <div class="brand brand--reversed">
      <div class="brand__dot"></div>
      <div class="brand__name">Brightline<br>Facades</div>
    </div>
    <p class="services">Storm Restoration, Roofing, Siding, Windows</p>
  </section>
</body>
</html>
```